Website re-fresh for a Medical Device company

We are looking to do a refresh of the website for Halvorsen Vital Devices, they invent/build devices for the medical industry revolving around Resuscitation.

http://halvitaldev.com/

They are currently marketing a single product but will be launching a 2nd product in the coming months pending certain medical certifications. The devices these guys engineer save lives, in the 12 places this new device is going through trials at the moment it’s already brought 80 people back to life.

I look at their current site and that just doesn’t tell me that story.

The people visiting this site will be:

* Doctors/Medical practitioners/EMC wanting to find out more information about their products. They’ll likely want to watch videos and read2 white-papers

* The products are bought by Hospitals/EMC/Fireman/Ambulance procurement staff. These visitors will likely have been given approval to purchase the product and are looking to find their nearest Distributor.

They're a very "proud to be American" company, but by no means in an ostentatious way. They're proud that it has been designed and engineered in the USA. They are trying to educate people about their products and the lives that they save.

It is not and e-commerce site, their products are distributed and marketed independently by Distributors. It is a Marketing/Splash site. The logo is apparently off-limits … I've attached a crappy version of the logo, good luck with a google images search. I've bought an option for a logo upgrade, I really doubt that is on the menu but ya never know.

We are only after the PSD designs, we will build it ourselves. We’re down a designer who went out on early maternity leave and I thought I’d see what you crazy crowd-sourced cats can come up with. I figure once we've picked a winner it will end up in some additional work, there will be probably 5-8 different page templates that I'll need help with.

Thanks and good luck!

Reason: Sorry .... the customer went offline for 2 weeks.

Target Market(s)

Medical professionals and EMC workers learning about their products and procurement staff who are turning up to find the details of a Distributor of their products

Industry/Entity Type

Medical Equipment

Logo Text

Halvorsen Vital Devices

Number of Pages Required

2 page

Requirements
Must have
• Responsive designs for 2 pages:
• a homepage showcasing their 2 products (old/new)
• a product page (http://halvitaldev.com/product/product/).
• Please keep the key users mentioned in the description in mind and what they'll be turning up to do.
Nice to have
• A customer should feel like they're visiting a website where the products these guys make save lives.
• It should be designed with the eye to being ADA friendly

```html
<!DOCTYPE html>
<html lang="en">
<head>
<meta charset="utf-8">
<title>Halvorsen Vital Devices — Home</title>
<link rel="stylesheet" href="https://fonts.googleapis.com/css2?family=Open+Sans:wght@400;600;700&display=swap">
<style>
  :root {
    --hero-light: #e4e4e6;
    --hero-mid: #c9c9cc;
    --hero-dark: #a9a9ad;
    --white: #ffffff;
    --nav-text: #3a3a3c;
    --band-white: #ffffff;
    --strip-grey: #e6e6e8;
    --accent-blue: #5b8fd6;
    --device-light: #f2f2f2;
    --device-dark: #2a2a2c;
  }
  * { box-sizing: border-box; margin: 0; padding: 0; }
  html, body { width: 1200px; height: 783px; overflow: hidden; background: var(--strip-grey); }
  body { font-family: "Open Sans", Arial, sans-serif; position: relative; }

  .hero {
    position: absolute; left: 0; top: 0; width: 1200px; height: 652px;
    background:
      linear-gradient(115deg, transparent 55%, rgba(255,255,255,0.35) 62%, transparent 70%),
      radial-gradient(ellipse at 70% 40%, var(--hero-light) 0%, var(--hero-mid) 55%, var(--hero-dark) 100%);
    overflow: hidden;
  }

  .brand {
    position: absolute; left: 36px; top: 44px; width: 260px;
    display: flex; flex-direction: column; align-items: center; gap: 14px;
  }
  .brand-mark {
    width: 52px; height: 52px; border-radius: 50%;
    border: 3px solid var(--white);
  }
  .brand-name {
    color: var(--white); font-size: 24px; font-weight: 600; line-height: 1.15; text-align: center;
  }

  .search {
    position: absolute; left: 1002px; top: 63px; width: 161px; height: 27px;
    border: 1.5px solid var(--nav-text); border-radius: 3px;
    display: flex; align-items: center; justify-content: space-between; padding: 0 8px;
    font-size: 10px; color: var(--nav-text);
  }
  .search svg { width: 12px; height: 12px; }

  .main-nav {
    position: absolute; left: 476px; top: 116px; right: 37px;
    display: flex; justify-content: space-between;
    font-size: 13px; font-weight: 600; color: var(--nav-text); text-transform: uppercase;
  }
  .main-nav a { color: inherit; text-decoration: none; padding-bottom: 5px; }
  .main-nav a.is-current { border-bottom: 2px solid var(--nav-text); }

  .hero-copy { position: absolute; left: 110px; top: 308px; width: 560px; color: var(--white); }
  .hero-title { font-size: 32px; font-weight: 600; line-height: 1.2; }
  .hero-text { margin-top: 38px; margin-left: 8px; font-size: 17px; line-height: 28px; width: 470px; }
  .read-more {
    display: inline-flex; align-items: center; justify-content: center;
    margin-top: 36px; margin-left: 8px; width: 167px; height: 41px;
    border: 2px solid var(--white); border-radius: 3px;
    color: var(--white); font-size: 15px; font-weight: 700; text-decoration: none;
  }

  .product-visual {
    position: absolute; left: 690px; top: 250px; width: 450px; height: 440px;
    border-radius: 48% 48% 30% 30% / 40% 40% 22% 22%;
    background: linear-gradient(160deg, var(--device-dark) 0%, #555558 22%, var(--device-light) 40%, #dcdcdc 80%, #bdbdbf 100%);
    z-index: 2;
  }

  .next-slide { position: absolute; left: 1060px; top: 318px; width: 62px; height: 120px; z-index: 3; }

  .content-band { position: absolute; left: 0; top: 652px; width: 1200px; height: 79px; background: var(--band-white); }
  .footer-strip { position: absolute; left: 0; top: 731px; width: 1200px; height: 52px; background: var(--strip-grey); }
</style>
</head>
<body>
  <header class="hero">
    <div class="brand">
      <span class="brand-mark"></span>
      <span class="brand-name">Halvorsen Vital Devices</span>
    </div>

    <div class="search">
      <span>Search</span>
      <svg viewBox="0 0 12 12" aria-hidden="true"><circle cx="5" cy="5" r="3.6" fill="none" stroke="#1a1a1a" stroke-width="1.6"/><line x1="7.7" y1="7.7" x2="11" y2="11" stroke="#1a1a1a" stroke-width="1.8"/></svg>
    </div>

    <nav class="main-nav">
      <a href="http://halvitaldev.com/" class="is-current">Home</a>
      <a href="#">Assistance</a>
      <a href="http://halvitaldev.com/product/product/">Product</a>
      <a href="#">FAQ's</a>
      <a href="#">News &amp; Updates</a>
      <a href="#">Partners</a>
      <a href="#">About &amp; Contact</a>
    </nav>

    <section class="hero-copy">
      <h1 class="hero-title">Currantlly, less than 8% people<br>who suffer cardiac arrest survive</h1>
      <p class="hero-text">Lorem ipsum dolor sit amet, consectetur adipiscing elit. Integer consequat cursus leo, at rutrum orci commodo euismod.</p>
      <a class="read-more" href="#">READ MORE</a>
    </section>

    <svg class="next-slide" viewBox="0 0 62 120" aria-label="Next slide">
      <polyline points="4,4 56,60 4,116" fill="none" stroke="var(--accent-blue)" stroke-width="4"/>
    </svg>
  </header>

  <div class="product-visual" role="img" aria-label="Product render of the white resuscitation device with black top cap and metal side fittings"></div>

  <section class="content-band"></section>
  <div class="footer-strip"></div>
</body>
</html>
```